Real Estate "For Sale" Sign for construction company

We need a sign that we can use to hang on a post and place on the road when we sell a property. The sign will be simple and will need to mainly feature our logo (files attached), as well as the words "For Sale", and then our phone number "(555) 617 3489". The sign will hang on a post that'll look something like the attached picture.

Target Market(s)

Home buyers

Industry/Entity Type

Real Estate

Font styles to use
Serif
Sans Serif

Colors
0054AA
0677BA
7BADD7
CADEEF
E8F1F8
0094D4
00A9DD
6FCCEA
C7EBF8
E9F6FB

Requirements
Must have
• For Sale & our phone number

```html
<!DOCTYPE html>
<html lang="en">
<head>
<meta charset="utf-8">
<title>For Sale Sign Concepts – Ridgeline Oak Homes</title>
<link href="https://fonts.googleapis.com/css2?family=Krona+One&display=swap" rel="stylesheet">
<style>
  :root {
    --navy: #13204c;
    --royal: #0a51a5;
    --mid-blue: #1a80c4;
    --brand-blue: #1778c0;
    --sky: #3ec8f2;
    --pale-sky: #9adcf6;
    --white: #ffffff;
    --page: #ffffff;
  }
  * { box-sizing: border-box; margin: 0; padding: 0; }
  html, body { width: 1200px; height: 1200px; overflow: hidden; background: var(--page); }
  body { position: relative; font-family: "Krona One", sans-serif; }

  .sign {
    position: absolute;
    width: 309px;
    height: 386px;
    background: var(--white);
    box-shadow: 6px 10px 22px rgba(0,0,0,0.28);
    overflow: hidden;
  }
  .sign--outlined { left: 151px; top: 172px; }
  .sign--accent   { left: 727px; top: 172px; }
  .sign--navy     { left: 151px; top: 672px; }
  .sign--banded   { left: 727px; top: 672px; }

  .brand {
    position: absolute;
    left: 0; right: 0;
    display: flex; flex-direction: column; align-items: center;
  }
  .brand__mark {
    width: 38px; height: 38px; border-radius: 50%;
    background: var(--brand-blue);
    margin-bottom: 10px;
  }
  .brand__name {
    font-size: 14px;
    color: var(--brand-blue);
    white-space: nowrap;
  }

  .rule { position: absolute; height: 2px; background: var(--sky); }
  .rule--white { background: var(--white); }

  .phone {
    position: absolute;
    font-size: 22px;
    color: var(--brand-blue);
    white-space: nowrap;
    text-align: center;
    line-height: 1;
  }
  .phone--light { color: var(--white); }

  .block { position: absolute; }
  .for-sale {
    position: absolute;
    color: var(--sky);
    white-space: nowrap;
    line-height: 1;
    letter-spacing: -1px;
  }
</style>
</head>
<body>

  <!-- Concept 1: white with navy panel -->
  <section class="sign sign--outlined">
    <div class="brand" style="top:58px;">
      <span class="brand__mark"></span>
      <span class="brand__name">Ridgeline Oak Homes</span>
    </div>
    <div class="rule" style="left:18px; width:273px; top:181px;"></div>
    <p class="phone" style="left:0; width:309px; top:202px;">(555) 617 3489</p>
    <div class="rule" style="left:18px; width:273px; top:247px;"></div>
    <div class="block" style="left:14px; top:270px; width:281px; height:92px; background:var(--navy);"></div>
    <p class="for-sale" style="left:14px; width:281px; top:298px; font-size:36px; text-align:center;">For Sale</p>
  </section>

  <!-- Concept 2: side stripe accent -->
  <section class="sign sign--accent">
    <div class="block" style="left:0; top:16px; width:29px; height:346px; background:var(--pale-sky);"></div>
    <div class="brand" style="left:29px; top:66px;">
      <span class="brand__mark"></span>
      <span class="brand__name">Ridgeline Oak Homes</span>
    </div>
    <div class="rule" style="left:41px; width:253px; top:181px;"></div>
    <p class="phone" style="left:29px; width:280px; top:202px; font-size:21px;">(555) 617 3489</p>
    <div class="rule" style="left:41px; width:253px; top:247px;"></div>
    <div class="block" style="left:0; top:270px; width:29px; height:69px; background:var(--royal);"></div>
    <div class="block" style="left:29px; top:270px; width:280px; height:69px; background:var(--navy);"></div>
    <div class="block" style="left:29px; top:339px; width:280px; height:23px; background:var(--mid-blue);"></div>
    <p class="for-sale" style="left:38px; top:286px; font-size:38px;">For Sale</p>
  </section>

  <!-- Concept 3: navy lower half -->
  <section class="sign sign--navy">
    <div class="brand" style="top:52px;">
      <span class="brand__mark"></span>
      <span class="brand__name">Ridgeline Oak Homes</span>
    </div>
    <div class="block" style="left:0; top:151px; width:309px; height:211px; background:var(--navy);"></div>
    <div class="rule" style="left:18px; width:273px; top:181px;"></div>
    <p class="phone phone--light" style="left:0; width:309px; top:202px;">(555) 617 3489</p>
    <div class="rule" style="left:18px; width:273px; top:247px;"></div>
    <p class="for-sale" style="left:0; width:309px; top:274px; font-size:40px; text-align:center;">For Sale</p>
  </section>

  <!-- Concept 4: stacked bands -->
  <section class="sign sign--banded">
    <div class="brand" style="top:52px;">
      <span class="brand__mark"></span>
      <span class="brand__name">Ridgeline Oak Homes</span>
    </div>
    <div class="block" style="left:0; top:151px; width:309px; height:20px; background:var(--sky);"></div>
    <div class="block" style="left:0; top:171px; width:309px; height:86px; background:var(--royal);"></div>
    <div class="rule rule--white" style="left:18px; width:273px; top:181px;"></div>
    <p class="phone phone--light" style="left:0; width:309px; top:202px;">(555) 617 3489</p>
    <div class="rule rule--white" style="left:18px; width:273px; top:247px;"></div>
    <div class="block" style="left:0; top:266px; width:309px; height:95px; background:var(--navy);"></div>
    <p class="for-sale" style="left:0; width:309px; top:292px; font-size:40px; text-align:center;">For Sale</p>
  </section>

</body>
</html>
```